Brocure for Brindle - Social Media Management

Brindle is a Dutch company in the market of Social Media growth. We need a brochure (digital/PDF) for our company. Please see attached word doc for the text and attached logo. The initial proposal can contain just the first 4 pages text of the word doc.

We use informal language in all our communication.

Slogan: Effectieve Social Media Marketing voor professionals en ondernemers

Website: brindlesm-voorbeeld.nl

Industry/Entity Type

Digital Marketing

Contact Information for Business Card

Contact details:

Gerrit ter Hoeve
gerrit@brindlesm-voorbeeld.nl
06-19573826

```html
<!DOCTYPE html>
<html lang="nl">
<head>
<meta charset="utf-8">
<title>Brindle – brochure</title>
<link href="https://fonts.googleapis.com/css2?family=Source+Sans+3:wght@400;600;700&display=swap" rel="stylesheet">
<style>
:root{
  --navy:#13254a;
  --navy-deep:#0d1b38;
  --orange:#ea6a23;
  --ink:#2b2f38;
  --paper:#ffffff;
  --paper-soft:#f1f2f5;
  --backdrop:#9b9b9e;
}
*{margin:0;padding:0;box-sizing:border-box}
html,body{width:808px;height:1200px;overflow:hidden;background:var(--backdrop);font-family:"Source Sans 3",sans-serif;color:var(--ink)}
.spread{position:absolute;left:67px;width:694px;height:491px;background:var(--paper);box-shadow:0 8px 10px rgba(0,0,0,.25)}
.spread--outer{top:66px}
.spread--inner{top:628px}
.page{position:absolute;top:0;width:347px;height:491px;overflow:hidden;background:linear-gradient(180deg,var(--paper) 60%,var(--paper-soft))}
.page--left{left:0}
.page--right{left:347px;box-shadow:inset 8px 0 10px -8px rgba(0,0,0,.2)}
.abs{position:absolute}
.photo{position:absolute}
.brand{position:absolute;display:flex;align-items:center;gap:4px}
.brand__dot{width:18px;height:18px;border-radius:50%;border:2.5px solid var(--orange)}
.brand__name{font-weight:700;font-size:21px;color:var(--orange);letter-spacing:.5px;line-height:1}
.brand__sub{font-size:6px;font-weight:600;color:var(--navy);letter-spacing:.8px;margin-top:1px}
.h-orange{color:var(--orange);font-weight:600;font-size:9.5px;letter-spacing:.2px}
.h-navy{color:var(--navy);font-weight:700;font-size:7.5px}
.body{font-size:5.3px;line-height:1.3;color:var(--ink)}
.body p+p{margin-top:4px}
.step{position:absolute;left:46px;width:290px}
.step__title{font-size:5.6px;font-weight:700;color:var(--navy);margin-bottom:1px}
.step__icon{position:absolute;left:-30px;top:-2px;width:20px;height:20px;border-radius:50%;background:var(--navy);border:2px solid #c9cdd6;display:flex;align-items:center;justify-content:center}
.step__icon svg{width:10px;height:10px;fill:none;stroke:#fff;stroke-width:1.4;stroke-linecap:round;stroke-linejoin:round}
.timeline{position:absolute;left:26px;width:1.2px;background:var(--navy)}
.footer{position:absolute;left:0;bottom:0;width:347px;height:22px;background:var(--navy);border-top:2px solid var(--orange);display:flex;align-items:center;color:#fff;font-size:7px;letter-spacing:.3px}
.footer span{display:flex;align-items:center;gap:3px}
.footer i{display:inline-block;width:6px;height:6px;border:1px solid #fff;border-radius:50%}
.flow__box{position:absolute;top:95px;width:42px;height:41px;border-radius:4px;border:1.2px solid var(--navy);background:#fff;display:flex;align-items:center;justify-content:center}
.flow__box svg{width:24px;height:24px;fill:none;stroke:var(--navy);stroke-width:1.4;stroke-linecap:round;stroke-linejoin:round}
.flow__box--orange{border-color:var(--orange)}
.flow__box--orange svg{stroke:var(--orange)}
.flow__num{position:absolute;top:-7px;right:-6px;width:12px;height:12px;border-radius:50%;background:var(--navy);color:#fff;font-size:6px;font-weight:700;display:flex;align-items:center;justify-content:center}
.flow__num--orange{background:var(--orange)}
.band{position:absolute;left:0;top:326px;width:347px;height:165px;background:var(--navy)}
.band .body{color:#fff}
.platforms li{list-style:none;display:flex;align-items:center;gap:4px;font-size:5.3px;color:#fff;height:13px}
.platforms li i{width:9px;height:9px;border:1px solid #fff;border-radius:2px}
.sec-title{display:flex;align-items:center;gap:4px;font-weight:700;font-size:8px;color:var(--navy)}
.sec-title i{width:11px;height:11px;border-radius:50%;border:2px solid var(--orange)}
.band .sec-title{color:var(--orange)}
</style>
</head>
<body>

<section class="spread spread--outer">
  <div class="page page--left">
    <div class="photo" role="img" aria-label="Foto van bovenaf: handen aan een houten tafel met tablets, koffie en social-media-iconen" style="left:0;top:0;width:347px;height:150px;border-bottom-left-radius:42px;background:linear-gradient(135deg,#8a6a4c,#b88f66 45%,#6f5540)"></div>

    <div class="brand" style="left:98px;top:164px">
      <div class="brand__dot"></div>
      <div>
        <div class="brand__name">BRINDLE</div>
        <div class="brand__sub">SOCIAL MEDIA MARKETING</div>
      </div>
    </div>

    <div class="h-orange abs" style="left:15px;top:200px">HOE WERKT HET?</div>

    <div class="timeline" style="top:228px;height:192px"></div>

    <div class="step" style="top:220px">
      <div class="step__icon"><svg viewBox="0 0 12 12"><circle cx="5" cy="5" r="3.3"/><path d="M7.5 7.5L10.5 10.5"/></svg></div>
      <div class="step__title">QUICK SCAN &amp; ADVIES</div>
      <div class="body">We starten altijd met een grondige analyse van je website en sociale kanalen. Op basis daarvan geven we je een advies over de beste strategie.</div>
    </div>
    <div class="step" style="top:250px">
      <div class="step__icon"><svg viewBox="0 0 12 12"><circle cx="6" cy="6" r="2"/><path d="M6 1v2M6 9v2M1 6h2M9 6h2M2.5 2.5l1.4 1.4M8.1 8.1l1.4 1.4M2.5 9.5l1.4-1.4M8.1 3.9l1.4-1.4"/></svg></div>
      <div class="step__title">JE WILT MET ONS IN ZEE</div>
      <div class="body">
        <p>Als je besluit met ons in zee te gaan, doen we dat niet voor een paar weken. Want we doen niet aan hit-and-run, maar bouwen aan samenwerking die op de lange termijn echte resultaten oplevert. We moeten elkaar goed leren kennen en dat vraagt tijd.</p>
        <p>Je vertrouwt ons je sociale mediakanalen toe. Dat vraagt vertrouwen en tegelijk moeten wij ons goed inleven in de manier van communicatie die past bij jouw business en jouw doelgroep. Van beide kanten vraagt dit een tijdsinvestering.</p>
      </div>
    </div>
    <div class="step" style="top:316px">
      <div class="step__icon"><svg viewBox="0 0 12 12"><rect x="1.5" y="2" width="9" height="8" rx="1"/><path d="M1.5 4.5h9M4 6.5h4M4 8h3"/></svg></div>
      <div class="step__title">PAKKETKEUZE</div>
      <div class="body">We hebben verschillende servicepakketten waaruit je kunt kiezen wat bij jouw situatie en wensen past. Blijkt op basis van de QuickScan dat je beter af bent met maatwerk, dan maken we daarover specifieke afspraken. Geen twee klanten zijn gelijk, daarom is ons aanbod flexibel opgebouwd.</div>
    </div>
    <div class="step" style="top:354px">
      <div class="step__icon"><svg viewBox="0 0 12 12"><path d="M4.3 8.5h3.4M4.6 10.3h2.8M4.3 8.5C4.3 7 2.8 6.4 2.8 4.6a3.2 3.2 0 016.4 0c0 1.8-1.5 2.4-1.5 3.9"/></svg></div>
      <div class="step__title">IMPLEMENTATIE</div>
      <div class="body">
        <p>Natuurlijk wil je zo snel mogelijk resultaat zien. Dat willen wij ook. We werken de strategie uit in een plan en gaan voor jou aan het werk. Met de prioriteit op die gebieden die zo snel mogelijk resultaten opleveren. Omdat we graag (laten) zien dat onze inspanningen verschil maken.</p>
        <p>We richten daarvoor de benodigde systemen in. In het begin hebben we regelmatig overleg om elkaar goed te leren kennen en de vinger aan de pols te houden.</p>
      </div>
    </div>
    <div class="step" style="top:414px">
      <div class="step__icon"><svg viewBox="0 0 12 12"><path d="M10 6a4 4 0 11-1.2-2.9"/><path d="M9.2 1.2v2.2H7"/></svg></div>
      <div class="step__title">TERUGKOPPELING EN VERBETERING</div>
      <div class="body">Iedere ondernemer is gedreven als het gaat om het behalen van resultaten. Zo ook wij. Wij doen er alles aan om onze dienstverlening zo succesvol mogelijk te laten zijn en jouw sociale doelen te behalen. We hebben regelmatig contact om de resultaten te bespreken en daar waar mogelijk te verbeteren.</div>
    </div>

    <div class="footer" style="justify-content:space-around;font-size:6.4px">
      <span><i></i>gerrit@brindlesm-voorbeeld.nl</span>
      <span><i></i>06-19573826</span>
      <span><i></i>www.brindlesm-voorbeeld.nl</span>
    </div>
  </div>

  <div class="page page--right">
    <svg class="photo" width="347" height="360" viewBox="0 0 347 360" style="left:0;top:0">
      <defs>
        <linearGradient id="coverPhoto" x1="0" y1="0" x2="1" y2="1">
          <stop offset="0" stop-color="#e9ecf2"/>
          <stop offset=".35" stop-color="#b07a5a"/>
          <stop offset=".7" stop-color="#5d6f8e"/>
          <stop offset="1" stop-color="#c9b7a4"/>
        </linearGradient>
      </defs>
      <path role="img" aria-label="Foto: vijf lachende jongeren op een bank met laptop en tablets, met getekende social-media-schetsjes erboven" d="M0 0H330C338 90 336 200 290 262C240 330 140 348 0 330Z" fill="url(#coverPhoto)"/>
      <path d="M0 342C130 362 250 330 300 262" fill="none" stroke="var(--navy)" stroke-width="3"/>
      <path d="M328 10C350 120 330 250 270 318" fill="none" stroke="var(--orange)" stroke-width="4"/>
    </svg>

    <div class="brand" style="left:96px;top:369px">
      <div class="brand__dot"></div>
      <div>
        <div class="brand__name">BRINDLE</div>
        <div class="brand__sub">SOCIAL MEDIA MARKETING</div>
      </div>
    </div>

    <div class="abs" style="left:0;width:347px;top:405px;text-align:center;color:var(--navy);font-size:12.5px;font-weight:600;line-height:1.25">SOCIAL MEDIA MARKETING VOOR ZAKELIJKE<br>PROFESSIONALS EN ONDERNEMERS</div>
    <div class="abs h-orange" style="left:0;width:347px;top:441px;text-align:center;font-size:9.5px">GROEI • INTERACTIE • EN CONTENT</div>

    <div class="footer" style="justify-content:center;font-size:8px"><span><i></i>www.brindlesm-voorbeeld.nl</span></div>
  </div>
</section>

<section class="spread spread--inner">
  <div class="page page--left">
    <div class="h-orange abs" style="left:15px;top:25px">GROEI • INTERACTIE • EN CONTENT</div>
    <div class="body abs" style="left:15px;top:42px;width:320px">Je bereik vergroten, traffic genereren en daarmee meer omzet behalen. Dat is wat wij bieden.<br>Onze services helpen jouw bereik op de sociale media te vergroten. Met een uitgekiende groeistrategie, onze kennis en geavanceerde tools zorgen we voor gerichte content en interactie op je sociale netwerken.</div>

    <svg class="abs" style="left:0;top:75px" width="347" height="70">
      <path d="M36 20V13Q36 8 41 8H55M293 8H307Q312 8 312 13V20" fill="none" stroke="var(--navy)" stroke-width="1"/>
      <circle cx="55" cy="8" r="1.8" fill="var(--navy)"/><circle cx="293" cy="8" r="1.8" fill="var(--navy)"/>
      <line x1="57" y1="40" x2="85" y2="40" stroke="var(--navy)"/>
      <line x1="127" y1="40" x2="153" y2="40" stroke="var(--navy)"/>
      <line x1="195" y1="40" x2="222" y2="40" stroke="var(--navy)"/>
      <line x1="264" y1="40" x2="292" y2="40" stroke="var(--navy)"/>
    </svg>
    <div class="abs" style="left:58px;top:79px;font-size:4.6px;font-weight:600;color:var(--navy)">((ACTIEVE INTERACTIE + RELEVANTE CONTENT) &gt; ACTIEVE VOLGERS) = (&gt; TRAFFIC + OMZET)</div>

    <div class="flow__box" style="left:15px"><div class="flow__num">1</div>
      <svg viewBox="0 0 24 24"><circle cx="10" cy="9" r="6"/><path d="M7.5 9l2 2 3.5-4"/><path d="M13 14v6M11 17h6v4h-6z"/></svg></div>
    <div class="flow__box flow__box--orange" style="left:85px"><div class="flow__num flow__num--orange">2</div>
      <svg viewBox="0 0 24 24"><path d="M5 3h10l3 3v15H5z"/><path d="M8 8h6M8 11h4M8 14h3"/><rect x="13" y="14" width="6" height="5" rx="1"/><path d="M14.5 14v-1.5a1.5 1.5 0 013 0V14"/></svg></div>
    <div class="flow__box" style="left:153px"><div class="flow__num">3</div>
      <svg viewBox="0 0 24 24"><circle cx="7" cy="8" r="2.2"/><circle cx="12" cy="6.5" r="2.2"/><circle cx="17" cy="8" r="2.2"/><path d="M3 15q4-5 18 0M3 19h4l4 2 9-4"/></svg></div>
    <div class="flow__box flow__box--orange" style="left:223px"><div class="flow__num flow__num--orange">4</div>
      <svg viewBox="0 0 24 24"><circle cx="12" cy="13" r="7"/><path d="M12 13V9M10 3h4M12 3v3M18 6l1.5-1.5"/></svg></div>
    <div class="flow__box" style="left:292px"><div class="flow__num">5</div>
      <svg viewBox="0 0 24 24"><rect x="3" y="4" width="18" height="12" rx="1"/><path d="M9 20h6M12 16v4"/><circle cx="12" cy="10" r="2"/><path d="M12 6.5v1M12 12.5v1M8.5 10h1M14.5 10h1"/></svg></div>

    <div class="abs" style="left:15px;top:162px;width:152px">
      <div class="h-navy">WIE ZIJN WIJ?</div>
      <div class="body" style="margin-top:4px;text-align:justify">Wij zijn Brindle. Een team van sociale media experts dat je sociale netwerk activeert en het bereik vergroot. We zorgen voor sociale interactie met volgers, nieuwe en bestaande. Daarmee genereren we traffic naar je website/shop.<br>Het doel? Meer omzet. Simpel en heel meetbaar.</div>
      <div class="h-navy" style="margin-top:18px">VOOR WIE?</div>
      <div class="body" style="margin-top:2px;text-align:justify">Onze dienstverlening kan ingezet worden op zowel persoonlijke zakelijke profielen (bv Linkhub), of voor bedrijfspagina's op diverse sociale mediakanalen.</div>
    </div>

    <div class="abs" style="left:180px;top:162px;width:155px">
      <div class="h-navy">WAT DOEN WE?</div>
      <div class="body" style="margin-top:4px;text-align:justify">
        <p>Samen met jou bepalen we je doelen in de sociale netwerken. Zowel strategisch als tactisch en operationeel. Wij richten ons op die doelen en zorgen voor een netwerk van echte en actieve volgers.</p>
        <p>Of het nu gaat om Linkhub, Snapgram, Facenet of Chirper, interactie zorgt voor betrokken volgers. Die jij vervolgens in je verkoopproces kunt oppakken.</p>
        <p>Voor zakelijke professionals verzorgen wij personal branding met als doel impact en social sales. We zorgen voor veel meer relevante connecties en activeren je zakelijke netwerk. Gecombineerd met de juiste contentstrategie, zorgen wij ervoor dat je gezien wordt als autoriteit in je vakgebied.</p>
        <p>Onze diensten voor bedrijven bestaan uit de versnelde organische groei van het volgernetwerk, het activeren van het netwerk met content en interactie. We zorgen daarmee voor een groot bereik en verkeer naar je website.</p>
      </div>
    </div>

    <div class="band"></div>
    <svg class="photo" width="190" height="200" viewBox="0 0 190 200" style="left:0;top:291px">
      <path role="img" aria-label="Foto: lachende vrouw met krullend haar die op haar smartphone kijkt" d="M0 12Q100 0 150 60Q178 100 172 200H0Z" fill="#a7795a"/>
      <path d="M0 6Q110 -6 160 60Q186 100 180 200" fill="none" stroke="var(--orange)" stroke-width="3"/>
    </svg>

    <div class="abs" style="left:188px;top:362px">
      <div class="h-orange">WELKE PLATFORMEN?</div>
      <div style="font-size:4.8px;color:var(--orange);margin:2px 0 4px">We bieden onze diensten aan op alle belangrijke platformen:</div>
      <ul class="platforms">
        <li><i></i>Linkhub (bedrijfspagina's en persoonlijke profielen)</li>
        <li><i></i>Facenet (bedrijfspagina's en groepen)</li>
        <li><i></i>Snapgram (bedrijfspagina's en persoonlijke profielen)</li>
        <li><i></i>Chirper</li>
        <li><i></i>Vidstream</li>
        <li><i></i>Zoekgids Bedrijf</li>
        <li><i></i>Optioneel: Clipclap, Prikbord, Threadly en Blogbox</li>
      </ul>
    </div>
  </div>

  <div class="page page--right">
    <div class="photo" role="img" aria-label="Foto: vijf mensen op een bank die borden met social-media-iconen voor hun gezicht houden" style="left:0;top:0;width:347px;height:137px;border-bottom-right-radius:18px;background:linear-gradient(90deg,#5b4636,#7a6a60 30%,#3d4a66 60%,#6a5a4e)"></div>

    <div class="abs" style="left:12px;top:166px;width:158px">
      <div class="sec-title"><i></i>WAAROM KIES JE VOOR ONS?</div>
      <div class="body" style="margin-top:3px;text-align:justify">
        <p>Jij hebt jouw vak, wij het onze. Als iedereen doet waar hij goed in is, worden daar allemaal beter van. Wij zijn goed in het activeren en vergroten van je sociale netwerk. Daarvoor gebruiken we een slimme mix van kennis en tools.</p>
        <p>Een strategie die ervoor zorgt dat jij je kunt focussen op je corebusiness. Met onze slimme tools vergroten wij de impact van je sociale netwerken. Met als resultaat: meer traffic, meer leads, meer omzet.</p>
      </div>
      <div class="sec-title" style="margin-top:11px"><i></i>DOEN WE ALLES ZELF?</div>
      <div class="body" style="margin-top:3px;text-align:justify">Wij zijn slim in de strategie en systemen voor het vergroten van interactie. En we hebben een netwerk van specialisten die slim zijn in hun vak. Zoals een reclamebureau, creatief ontwerper, websitebouwer of marketingstrategiebureau. Is er op dat vlak een behoefte, dan brengen wij je graag in contact.</div>
    </div>

    <div class="abs" style="left:180px;top:166px;width:156px">
      <div class="sec-title"><i></i>VOLLEDIG SOCIAAL MANAGEMENT</div>
      <div class="body" style="margin-top:3px;text-align:justify">We bieden een compleet beheerpakket voor sociale media waarmee we betrokkenheid van volgers realiseren en tijdig en altijd proactief schakelen naar de volgende stap. Zo blijven bezoekers geboeid en actief.<br>We plannen zowel doelgroep- als branche specifieke inhoud en combineren online aanwezigheid om meer en meer gericht websiteverkeer te genereren.</div>
      <div class="sec-title" style="margin-top:8px"><i></i>ACTIVEREN VAN JE NETWERK</div>
      <div class="body" style="margin-top:3px;text-align:justify">
        <p>Je bent al een poos bezig met het beheren van je sociale media, maar ziet geen commercieel resultaat? De specialist maakt het verschil. Jouw kennis van jouw product en klant, gecombineerd met ons specialisme over sociale media. In zeer diverse branches.</p>
        <p>Wij gebruiken deze kennis voor een contentstrategie op maat. Een strategie die gegarandeerd meer likes, retweets en doorkliks genereert. Meer likes, meer interactie, meer betrokkenheid: meer omzet.</p>
      </div>
    </div>

    <div class="band">
      <div class="abs" style="left:12px;top:18px;width:158px">
        <div class="sec-title"><i></i>GROEIEN OP SOCIALE MEDIA</div>
        <div class="body" style="margin-top:4px;text-align:justify">
          <p>Het staat als een paal boven water: sociale media zijn een krachtig marketinginstrument. Een kans die je niet voorbij kunt laten gaan, of je dat nou leuk vindt of niet. Het geeft je de kans om je merk op te bouwen, je zicht- en vindbaarheid te verbeteren en uiteindelijk meer leads en verkopen te genereren.</p>
          <p>Het beheren van je sociale platforms is een tijdrovende klus. En om resultaat te krijgen, moet je het ook nog eens slim doen. Om de online herkenbaarheid van je bedrijf te vergroten, zijn je uitingen de sleutel.</p>
          <p>Interactie, consistentie, responsiveness, allemaal zorgen ze voor herkenning en betrokkenheid van je volgers. We helpen je om je digitale activiteiten met elkaar te verbinden en je bedrijf te laten groeien.</p>
        </div>
      </div>
      <div class="abs" style="left:180px;top:18px;width:156px">
        <div class="sec-title"><i></i>GROEISTRATEGIE</div>
        <div class="body" style="margin-top:4px;text-align:justify">
          <p>Je netwerk op sociale media laten groeien kan een lastige klus zijn. Maar het levert je enorm veel op. Een groot aantal echte en actieve volgers geeft vertrouwen en genereert nog meer betrokkenheid.</p>
          <p>Het is de moderne variant van mond-tot-mondreclame.</p>
          <p>Wij hebben de expertise en oplossingen om al je profielen een echte boost te geven. Met onze tools krijgen we de volledige controle over je kanalen, zodat jij jouw focus kunt richten op de uitvoering en levering van opdrachten.</p>
          <p>En wees voorbereid op groei!</p>
        </div>
      </div>
    </div>
  </div>
</section>

</body>
</html>
```